Business Card Re-Design/Update

We'd like to update out business cards. I've included our current "Style guide" which has the colour scheme of the organisation in it. I've also included the branding files with logos etc in them.

I've also included a copy of one of our existing cards so that you can see how ugly/dated they look. I'd like a fresh modern corporate look.

Target Market(s)

These are for our clients, potential clients, industry contacts - like all business cards

Contact Information for Business Card

Name
Position
Company Address - Level 1, 47 Garnet Lane, Toowong Qld 4066
Direct Phone
mobile
Email
Website -www.korvalnet.com.au
Logo

Colors

Designer to choose colors to be used in the design.

Requirements
Must have
• Main Logo
• Cards will need to be editable to be able to personalize them for each new employee.
Nice to have
• The MapOUT, HandOVER, UpKEEP would be okay to have if they can be sensibly and professionally added to the look without detracting from the main imagery.
• Maybe they could go on the back of the card? will leave this to your creative discretion as to whether/where they fit.
Should not have
• Should not have decorative or script fonts

```html
<!DOCTYPE html>
<html lang="en">
<head>
<meta charset="utf-8">
<title>KorvalNet business card</title>
<link rel="stylesheet" href="https://fonts.googleapis.com/css2?family=Arimo:wght@400;700&family=Poppins:wght@500&display=swap">
<style>
  :root {
    --charcoal: #414042;
    --red: #d91f26;
    --orange: #e05a3a;
    --white: #ffffff;
    --ink: #231f20;
    --green: #5a9e3c;
    --blue: #2c8ccf;
    --magenta: #c2238f;
    --bg-start: #2b3468;
    --bg-end: #5ea6c4;
  }
  * { margin: 0; padding: 0; box-sizing: border-box; }
  html, body { width: 1200px; height: 1200px; overflow: hidden; }
  body {
    background: linear-gradient(90deg, var(--bg-start), var(--bg-end));
    font-family: "Arimo", Arial, sans-serif;
    position: relative;
  }
  .card {
    position: absolute;
    width: 738px;
    height: 422px;
    background: var(--white);
    overflow: hidden;
    transform: scale(0.8);
    transform-origin: 0 0;
  }
  .card--front { left: 305px; top: 201px; }
  .card--back { left: 306px; top: 597px; }
  .card__art { position: absolute; inset: 0; width: 738px; height: 422px; }

  .holder { position: absolute; left: 36px; top: 28px; color: var(--white); }
  .holder__name { font-weight: 700; font-size: 34px; letter-spacing: 0.2px; }
  .holder__surname { color: var(--red); }
  .holder__role { font-size: 20px; margin-top: 6px; }

  .contact-list { position: absolute; left: 0; top: 199px; width: 396px; list-style: none; }
  .contact-list__row { position: relative; height: 60px; background: var(--red); display: flex; align-items: center; }
  .contact-list__row + .contact-list__row { margin-top: 0.5px; }
  .contact-list__row--alt { background: var(--orange); }
  .contact-list__icon {
    position: absolute; left: 27px; top: 0; width: 57px; height: 100%;
    background: var(--charcoal); display: flex; align-items: center; justify-content: center;
  }
  .contact-list__text { margin-left: 95px; color: var(--white); font-size: 19px; }

  .brand-name { font-family: "Poppins", Arial, sans-serif; font-weight: 500; color: var(--charcoal); }
  .card__brand { position: absolute; left: 462px; top: 196px; font-size: 30px; display: flex; align-items: center; gap: 10px; }
  .brand-mark { width: 18px; height: 18px; background: var(--red); }

  .company-info { position: absolute; left: 430px; top: 283px; color: var(--ink); font-size: 19px; }
  .company-info__item { display: flex; align-items: flex-start; gap: 10px; }
  .company-info__item + .company-info__item { margin-top: 14px; }
  .company-info__icon { width: 40px; flex: none; display: flex; justify-content: center; }

  .logo-panel {
    position: absolute; left: 125px; top: 27px; width: 498px; height: 161px;
    background: var(--white); display: flex; align-items: center; justify-content: center; gap: 18px;
  }
  .logo-panel .brand-name { font-size: 62px; }
  .logo-panel .brand-mark { width: 40px; height: 40px; }

  .service-list { position: absolute; left: 0; top: 336px; width: 738px; height: 50px; list-style: none; }
  .service { position: absolute; display: flex; align-items: center; gap: 8px; font-family: "Poppins", Arial, sans-serif; font-weight: 500; font-size: 30px; }
  .service__mark { width: 22px; height: 22px; background: currentColor; }
  .service--mapout { left: 40px; color: var(--green); }
  .service--handover { left: 281px; color: var(--blue); }
  .service--upkeep { left: 511px; color: var(--magenta); }
</style>
</head>
<body>

<section class="card card--front" aria-label="Business card front">
  <svg class="card__art" viewBox="0 0 738 422" aria-hidden="true">
    <path fill="var(--red)" d="M0,137 V183 C80,186 160,178 215,165 C150,170 70,160 0,137 Z"/>
    <path fill="var(--red)" d="M360,128 C450,108 520,98 570,100 C650,103 710,140 738,168 V194 C690,150 630,115 560,112 C480,110 420,118 360,128 Z"/>
    <path fill="var(--charcoal)" d="M0,0 H738 V160 C650,105 560,95 480,105 C380,120 300,165 190,163 C110,162 50,150 0,132 Z"/>
    <rect x="678" y="27" width="70" height="18" rx="9" fill="var(--red)"/>
    <rect x="678" y="55" width="70" height="18" rx="9" fill="var(--orange)"/>
    <rect x="678" y="83" width="70" height="18" rx="9" fill="var(--red)"/>
  </svg>

  <div class="holder">
    <div class="holder__name">Maren <span class="holder__surname">Whitfield</span></div>
    <div class="holder__role">Business Development Manager</div>
  </div>

  <ul class="contact-list">
    <li class="contact-list__row">
      <span class="contact-list__icon">
        <svg width="38" height="28" viewBox="0 0 38 28"><rect x="1" y="1" width="36" height="26" fill="none" stroke="#fff" stroke-width="2"/><path d="M1,1 L19,16 L37,1 M1,27 L15,13 M37,27 L23,13" fill="none" stroke="#fff" stroke-width="2"/></svg>
      </span>
      <span class="contact-list__text">mwhitfield@korvalnet.com.au</span>
    </li>
    <li class="contact-list__row contact-list__row--alt">
      <span class="contact-list__icon">
        <svg width="22" height="34" viewBox="0 0 22 34"><rect x="2" y="1" width="18" height="32" rx="3" fill="none" stroke="#fff" stroke-width="2.5"/><circle cx="11" cy="28" r="1.8" fill="#fff"/></svg>
      </span>
      <span class="contact-list__text">+61 (0)400 555 218</span>
    </li>
    <li class="contact-list__row">
      <span class="contact-list__icon">
        <svg width="38" height="30" viewBox="0 0 38 30"><path d="M2,10 C2,2 36,2 36,10 L29,12 L27,7 H11 L9,12 Z" fill="#fff"/><rect x="7" y="13" width="24" height="16" rx="2" fill="#fff"/><g fill="var(--charcoal)"><rect x="12" y="17" width="3" height="2"/><rect x="17.5" y="17" width="3" height="2"/><rect x="23" y="17" width="3" height="2"/><rect x="12" y="22" width="3" height="2"/><rect x="17.5" y="22" width="3" height="2"/><rect x="23" y="22" width="3" height="2"/></g></svg>
      </span>
      <span class="contact-list__text">+61 (0)7 3000 4812</span>
    </li>
  </ul>

  <div class="card__brand"><span class="brand-mark"></span><span class="brand-name">KorvalNet</span></div>

  <div class="company-info">
    <div class="company-info__item">
      <span class="company-info__icon">
        <svg width="36" height="36" viewBox="0 0 36 36" fill="none" stroke="var(--ink)" stroke-width="2.5"><circle cx="18" cy="18" r="16"/><ellipse cx="18" cy="18" rx="7" ry="16"/><path d="M2,18 H34 M5,10 H31 M5,26 H31"/></svg>
      </span>
      <span>www.korvalnet.com.au</span>
    </div>
    <div class="company-info__item">
      <span class="company-info__icon">
        <svg width="40" height="38" viewBox="0 0 40 38"><path d="M20,2 L39,19 L35,22 L20,9 L5,22 L1,19 Z" fill="var(--ink)"/><path d="M8,21 L20,11 L32,21 V37 H24 V27 H16 V37 H8 Z" fill="var(--ink)"/><rect x="29" y="4" width="5" height="9" fill="var(--ink)"/></svg>
      </span>
      <span>Level 1, 47 Garnet Lane,<br>Toowong Qld 4066</span>
    </div>
  </div>
</section>

<section class="card card--back" aria-label="Business card back">
  <svg class="card__art" viewBox="0 0 738 422" aria-hidden="true">
    <rect x="0" y="0" width="738" height="100" fill="var(--charcoal)"/>
    <g transform="translate(0,97)">
      <path fill="var(--red)" d="M0,137 V183 C80,186 160,178 215,165 C150,170 70,160 0,137 Z"/>
      <path fill="var(--red)" d="M360,128 C450,108 520,98 570,100 C650,103 710,140 738,168 V194 C690,150 630,115 560,112 C480,110 420,118 360,128 Z"/>
      <path fill="var(--charcoal)" d="M0,0 H738 V160 C650,105 560,95 480,105 C380,120 300,165 190,163 C110,162 50,150 0,132 Z"/>
    </g>
  </svg>

  <div class="logo-panel"><span class="brand-mark"></span><span class="brand-name">KorvalNet</span></div>

  <ul class="service-list">
    <li class="service service--mapout"><span class="service__mark"></span>MapOUT</li>
    <li class="service service--handover"><span class="service__mark"></span>HandOVER</li>
    <li class="service service--upkeep"><span class="service__mark"></span>UpKEEP</li>
  </ul>
</section>

</body>
</html>
```